Brightwave Business Card

Professional Business Card Design required using the attached contact information.

Contact information can be rearranged as required.

The company is a new start up venture developing solar systems, the branding should be in keeping with that of one of the investors whose website is as follows https://www.quorvex.com/

```html
<!DOCTYPE html>
<html lang="en">
<head>
<meta charset="utf-8">
<title>Brightwave Renewables Business Card</title>
<link href="https://fonts.googleapis.com/css2?family=Montserrat:wght@500;600&family=Roboto:wght@400&display=swap" rel="stylesheet">
<style>
  :root {
    --canvas-bg: #d6d6d6;
    --brand-green: #285a48;
    --panel-white: #f2f2f2;
    --band-dark: #2c2f2e;
    --text-light: #ffffff;
    --text-soft: #e3ece8;
    --wordmark-grey: #3a3d3c;
  }
  * { margin: 0; padding: 0; box-sizing: border-box; }
  html, body { width: 1200px; height: 576px; overflow: hidden; background: var(--canvas-bg); }
  .canvas { position: relative; width: 1200px; height: 576px; }
  .card {
    position: absolute; top: 138px; width: 484px; height: 294px;
    border-radius: 10px; overflow: hidden; background: var(--brand-green);
    box-shadow: 0 2px 5px rgba(0,0,0,0.25);
  }
  .card-front { left: 82px; }
  .card-back { left: 602px; width: 481px; }
  .front-wordmark {
    position: absolute; left: 0; right: 0; top: 50%; transform: translateY(-50%);
    text-align: center; color: var(--text-soft);
    font-family: "Montserrat", sans-serif; font-weight: 500; line-height: 1.0;
  }
  .front-wordmark .line-1 { display: block; font-size: 30px; letter-spacing: 0.5px; }
  .front-wordmark .line-2 { display: block; font-size: 24px; margin-top: 1px; }
  .back-shape { position: absolute; inset: 0; }
  .holder { position: absolute; left: 28px; top: 32px; color: var(--text-light); font-family: "Roboto", sans-serif; }
  .holder-name { font-family: "Montserrat", sans-serif; font-weight: 600; font-size: 20px; line-height: 1.2; }
  .holder-title { font-size: 12px; margin-top: 3px; color: var(--text-soft); }
  .contact-list { position: absolute; left: 28px; top: 184px; list-style: none; font-family: "Roboto", sans-serif; font-size: 12.5px; color: var(--text-soft); }
  .contact-list li { display: flex; align-items: center; height: 20.5px; }
  .contact-list svg { width: 12px; height: 12px; margin-right: 12px; fill: var(--text-soft); flex: none; }
  .side-wordmark {
    position: absolute; left: 414px; top: 150px;
    transform: translate(-50%, -50%) rotate(-90deg);
    font-family: "Montserrat", sans-serif; font-weight: 600; color: var(--wordmark-grey);
    font-size: 27px; line-height: 0.95; white-space: nowrap; text-align: left;
  }
  .side-wordmark span { display: block; }
</style>
</head>
<body>
<div class="canvas">
  <section class="card card-front">
    <div class="front-wordmark">
      <span class="line-1">BRIGHTWAVE</span>
      <span class="line-2">RENEWABLES</span>
    </div>
  </section>

  <section class="card card-back">
    <svg class="back-shape" viewBox="0 0 481 294" preserveAspectRatio="none" aria-hidden="true">
      <path d="M318 0 C 286 70, 292 210, 344 294 L 350 294 C 300 210, 294 70, 330 0 Z" fill="var(--band-dark)"/>
      <path d="M328 0 C 294 70, 300 210, 350 294 L 481 294 L 481 0 Z" fill="var(--panel-white)"/>
    </svg>

    <div class="holder">
      <div class="holder-name">Daniel Hartwell</div>
      <div class="holder-title">Managing Director</div>
    </div>

    <ul class="contact-list">
      <li><svg viewBox="0 0 24 24"><path d="M3 9c0-3 4-5 9-5s9 2 9 5v2h-5V9H8v2H3zM6 12h12l2 8H4z"/></svg>+1 (555) 014-2270</li>
      <li><svg viewBox="0 0 24 24"><path d="M12 2a10 10 0 1 0 0 20 10 10 0 0 0 0-20zm6.9 9h-3a15 15 0 0 0-1.3-6 8 8 0 0 1 4.3 6zM12 4c.9 1.3 1.8 3.8 2 7h-4c.2-3.2 1.1-5.7 2-7zM9.4 5a15 15 0 0 0-1.3 6h-3a8 8 0 0 1 4.3-6zM5.1 13h3a15 15 0 0 0 1.3 6 8 8 0 0 1-4.3-6zM12 20c-.9-1.3-1.8-3.8-2-7h4c-.2 3.2-1.1 5.7-2 7zm2.6-1a15 15 0 0 0 1.3-6h3a8 8 0 0 1-4.3 6z"/></svg>www.brightwave-renewables.com</li>
      <li><svg viewBox="0 0 24 24"><path d="M2 5h20v14H2zm2 2v1l8 5 8-5V7l-8 5z"/></svg>daniel.hartwell@brightwave-renewables.com</li>
      <li><svg viewBox="0 0 24 24"><path d="M12 2a7 7 0 0 0-7 7c0 5 7 13 7 13s7-8 7-13a7 7 0 0 0-7-7zm0 9.5A2.5 2.5 0 1 1 12 6.5a2.5 2.5 0 0 1 0 5z"/></svg>218 Harbor Street, Boston, MA 02110</li>
    </ul>

    <div class="side-wordmark">
      <span>BRIGHTWAVE</span>
      <span>RENEWABLES</span>
    </div>
  </section>
</div>
</body>
</html>
```